Business Card Design

I am a florist specialising in weddings. I would like a very modern however elegant and simple design. My arrangement designs can be quite rustic with a vintage feel, so if you are able to reflect this in the card that would be great.
Updates

Thank you everyone for your submissions. I have found some further words for inspiration. I am looking for something more earthy and artisan looking. If possible I would like to use 100% recycled paper - the type that even looks rustic and recycled. I may even opt to use a small logo to emphasis the fact that they are made from recycled paper. I know this is quite different to my original brief but I wasn't quite sure what to expect from your designs. Also, with the logo, I give permission for it to be cropped to remove the 'Floral Designer' text. Please contact me if you need any further assistance. Many thanks Lisette Petal and Thistle Studio

I would prefer not to have any photgraphs & not too much pink. Thank you!

Industry/Entity Type

Florist

Contact Information for Business Card

Lisette Varko
Floral Designer
0417 365 820
lisette@petalthistlestudio.com.au
petalthistlestudio.com.au

Requirements
Must have
• My logo

```html
<!DOCTYPE html>
<html lang="en">
<head>
<meta charset="utf-8">
<title>Petal and Thistle Studio — Business Cards</title>
<link rel="stylesheet" href="https://fonts.googleapis.com/css2?family=Almendra&family=Cinzel:wght@400&family=Questrial&display=swap">
<style>
  :root {
    --backdrop: #e2e2e2;
    --card: #ffffff;
    --ink: #111111;
    --accent-pink: #e0336f;
    --rule-pink: #f2a9c0;
    --name-red: #8c1d24;
    --divider-red: #b5474d;
    --mark-pink: #d46a9a;
  }
  * { margin: 0; padding: 0; box-sizing: border-box; }
  html, body {
    width: 1000px; height: 1200px; overflow: hidden;
    background: var(--backdrop);
  }
  .canvas { position: relative; width: 1000px; height: 1200px; }

  .card {
    position: absolute; width: 722px; height: 422px;
    background: var(--card);
  }
  .card--front { left: 147px; top: 153px; }
  .card--back  { left: 165px; top: 670px; }

  .card__dash {
    position: absolute; left: 15px; right: 20px; height: 0;
    border-top: 1px dashed var(--accent-pink);
  }
  .card__dash--top { top: 22px; }
  .card__dash--bottom { bottom: 21px; }

  .brand {
    position: absolute; left: 0; right: 0; text-align: center;
    font-family: "Almendra", serif; color: var(--ink);
    white-space: nowrap;
  }
  .brand__dot {
    position: absolute; left: 50%; width: 26px; height: 26px;
    margin-left: -13px; border-radius: 50%; background: var(--mark-pink);
  }
  .card--front .brand { top: 138px; font-size: 39px; }
  .card--front .brand__dot { top: 78px; }
  .card--back .brand { top: 183px; font-size: 41px; }
  .card--back .brand__dot { top: 120px; }

  .person {
    position: absolute; left: 0; right: 0; top: 240px; text-align: center;
    font-family: "Cinzel", serif; font-size: 24px; letter-spacing: 2.5px;
    color: var(--name-red);
  }
  .role {
    position: absolute; left: 196px; width: 327px; top: 278px;
    display: flex; align-items: center; gap: 8px;
    font-family: "Questrial", sans-serif; font-size: 15px; letter-spacing: 1.3px;
    color: var(--accent-pink); white-space: nowrap;
  }
  .role__rule { flex: 1; height: 1px; background: var(--rule-pink); }

  .contacts {
    position: absolute; left: 0; right: 0; top: 347px;
    display: flex; justify-content: center; align-items: center;
    font-family: "Questrial", sans-serif; font-size: 12.5px; letter-spacing: 1.3px;
    color: var(--ink); white-space: nowrap;
  }
  .contacts__sep {
    width: 1px; height: 24px; background: var(--divider-red); margin: 0 12px;
  }

  .tagline {
    position: absolute; left: 0; right: 0; top: 272px; text-align: center;
    font-family: "Almendra", serif; font-size: 28px; color: var(--ink);
  }
</style>
</head>
<body>
<main class="canvas">
  <section class="card card--front">
    <div class="card__dash card__dash--top"></div>
    <span class="brand__dot"></span>
    <h1 class="brand">Petal and Thistle Studio</h1>
    <p class="person">LISETTE VARKO</p>
    <p class="role"><span class="role__rule"></span>Floral Designer<span class="role__rule"></span></p>
    <p class="contacts">
      <span>lisette@petalthistlestudio.com.au</span>
      <span class="contacts__sep"></span>
      <span>0417 365 820</span>
      <span class="contacts__sep"></span>
      <span>petalthistlestudio.com.au</span>
    </p>
    <div class="card__dash card__dash--bottom"></div>
  </section>

  <section class="card card--back">
    <div class="card__dash card__dash--top"></div>
    <span class="brand__dot"></span>
    <h2 class="brand">Petal and Thistle Studio</h2>
    <p class="tagline">Floral Designer</p>
    <div class="card__dash card__dash--bottom"></div>
  </section>
</main>
</body>
</html>
```